Fiber Arts Workshop: Business Cards & Stationery
Copper Kettle StitchHouse, LLC
Fiber Arts Workshop: Business Cards & Stationery - Hobbies
Creative Brief
Bright & Fun-filled
Marla Penrose
Principal
48 Birchwood Terrace #512 Millbrook, New Jersey 07322
marla.penrose@ckstitchhouse.example
www.ckstitchhouse.example
Fonts - you may use fonts other than those used in the logo if they enhance the design

```html
<!DOCTYPE html>
<html lang="en">
<head>
<meta charset="utf-8">
<title>Copper Kettle StitchHouse – Business Card</title>
<link href="https://fonts.googleapis.com/css2?family=Open+Sans:wght@400;600;700&display=swap" rel="stylesheet">
<style>
  :root {
    --backdrop: #e9e6e1;
    --frame-start: #4f7be0;
    --frame-end: #7650cf;
    --card-face: #ffffff;
    --ink: #3a3a3a;
    --ink-soft: #6b6b6b;
    --rule: #c9c9c9;
    --icon: #3a3a3a;
  }
  * { margin: 0; padding: 0; box-sizing: border-box; }
  html, body {
    width: 1200px; height: 914px; overflow: hidden;
    background: var(--backdrop);
    font-family: "Open Sans", Arial, sans-serif;
  }
  .business-card {
    position: absolute; left: 100px; top: 171px;
    width: 1000px; height: 572px;
    background: linear-gradient(135deg, var(--frame-start), var(--frame-end));
    padding: 28px;
    box-shadow: 0 12px 30px rgba(0,0,0,0.18);
  }
  .card-face {
    position: relative; width: 100%; height: 100%;
    background: var(--card-face);
    display: flex; align-items: center;
  }
  .brand-block {
    width: 50%; height: 100%;
    display: flex; align-items: center; justify-content: center; gap: 16px;
  }
  .brand-dot {
    width: 30px; height: 30px; border-radius: 50%;
    background: var(--frame-end); flex: none;
  }
  .brand-name {
    font-size: 36px; font-weight: 600; color: var(--ink);
    line-height: 1.15; letter-spacing: -0.5px;
  }
  .divider {
    position: absolute; left: 50%; top: 70px; bottom: 70px;
    width: 1px; background: var(--rule);
  }
  .contact-block {
    width: 50%; padding-left: 40px;
  }
  .person-name { font-size: 26px; font-weight: 700; color: var(--ink); }
  .person-title { font-size: 17px; color: var(--ink-soft); margin-bottom: 36px; }
  .contact-list { list-style: none; }
  .contact-item {
    display: flex; align-items: flex-start; gap: 12px;
    font-size: 16px; color: var(--ink); line-height: 1.45; margin-bottom: 4px;
  }
  .contact-icon { width: 18px; height: 18px; flex: none; margin-top: 3px; }
</style>
</head>
<body>
  <div class="business-card">
    <div class="card-face">
      <div class="brand-block">
        <span class="brand-dot"></span>
        <span class="brand-name">Copper Kettle<br>StitchHouse</span>
      </div>
      <div class="divider"></div>
      <div class="contact-block">
        <p class="person-name">Marla Penrose</p>
        <p class="person-title">Principal</p>
        <ul class="contact-list">
          <li class="contact-item">
            <svg class="contact-icon" viewBox="0 0 20 20"><circle cx="10" cy="10" r="10" fill="var(--icon)"/><path d="M5 10.5 10 6l5 4.5M6.5 9.5V14h7V9.5" fill="none" stroke="#fff" stroke-width="1.6"/></svg>
            <span>48 Birchwood Terrace #512<br>Millbrook, New Jersey 07322</span>
          </li>
          <li class="contact-item">
            <svg class="contact-icon" viewBox="0 0 20 20"><circle cx="10" cy="10" r="10" fill="var(--icon)"/><path d="M7 5.5l2 2.5-1.2 1.2a6 6 0 0 0 3 3L12 11l2.5 2-1 1.5C10 15 5 10 5.5 6.5z" fill="#fff"/></svg>
            <span>(973) 555-0148</span>
          </li>
          <li class="contact-item">
            <svg class="contact-icon" viewBox="0 0 20 20"><circle cx="10" cy="10" r="10" fill="var(--icon)"/><rect x="5" y="6.5" width="10" height="7" fill="none" stroke="#fff" stroke-width="1.4"/><path d="M5 6.5l5 4 5-4" fill="none" stroke="#fff" stroke-width="1.4"/></svg>
            <span>marla.penrose@ckstitchhouse.example</span>
          </li>
          <li class="contact-item">
            <svg class="contact-icon" viewBox="0 0 20 20"><circle cx="10" cy="10" r="10" fill="var(--icon)"/><circle cx="10" cy="10" r="5" fill="none" stroke="#fff" stroke-width="1.3"/><path d="M5 10h10M10 5c-2.5 3-2.5 7 0 10M10 5c2.5 3 2.5 7 0 10" fill="none" stroke="#fff" stroke-width="1.1"/></svg>
            <span>www.ckstitchhouse.example</span>
          </li>
        </ul>
      </div>
    </div>
  </div>
</body>
</html>
```